Norvale Email Signature Banners – Fabrication Capability Series

www.Norvale.com.au is an Australian engineering and fabrication company specialising in fabrication and welding of :
steel piping spools,
skids and frames,
small volume process steel tanks
and general steel fabrication
We require four distinct banner designs for use in Teldrin Quillmark email signatures. Each banner will highlight a specific capability while maintaining a consistent brand identity.
Deliverables
Four banners total:
Piping Spools Fabrication – focus on precision welding and stainless steel pipework
Skid & Frames Fabrication – highlight skid systems and structural frames
Small Steel Tanks Fabrication – show fabricated tanks and workshop craftsmanship
General Fabrication Solutions – broad steel fabrication theme for company-wide use
Dimensions: 600–700 px wide × 100 px high
Format: PNG (preferred), small file size prefered
Resolution: 72 dpi
Background: non-transparent, industrial or workshop setting
Text examples:
1. Piping Spools Fabrication
Option A: “Expert Fabrication Solutions for Process Piping”
Option B: “Precision Welding for Complex Systems”
Option C: “Delivering Quality in Every Spool”
Option D: “Engineered for Flow, Built for Strength”
2. Skid & Frames Fabrication
Option A: “Custom Engineered Modular Systems”
Option B: “Built Strong. Designed Smart.”
Option C: “Reliable Frames for Industrial Performance”
Option D: “Modular Fabrication for Seamless Integration”
3. Small Steel Tanks Fabrication
Option A: “Precision Built for Your Needs”
Option B: “Compact Strength. Proven Durability.”
Option C: “Fabricated for Performance and Longevity”
Option D: “Small Tanks. Big Reliability.”
4. General Fabrication Solutions
Option A: “Quality Craftsmanship, Proven Results”
Option B: “Your Partner in Precision Fabrication”
Option C: “Engineering Excellence in Every Weld”
Option D: “Australian Fabrication. Global Standards.”
Style Direction
Clean, professional, and engineering‑focused
Use Norvale brand colours
Blend photo realism with vector clarity (no heavy gradients)
Include subtle industrial textures or workshop imagery
Typography: bold sans‑serif, legible at small scale
Usage Context
These banners will appear at the bottom of staff email signatures via Quillmark Email Signature Tool for Teldrin 365, so clarity and fast loading are essential. No Logo is required in the banners.
Reference
Existing Norvale signature is attached. Colour palette to match the signature style and logo.
Target Market(s)
Engineering and construction companies,
Industry/Entity Type
Engineering fabrication design

```html
<!DOCTYPE html>
<html lang="en">
<head>
<meta charset="utf-8">
<title>Norvale Email Signature Banners – Fabrication Capability Series</title>
<link rel="stylesheet" href="https://fonts.googleapis.com/css2?family=Hind:wght@500;700&family=Poppins:wght@300&display=swap">
<style>
  :root {
    --page-glow: #0a62c4;
    --page-deep: #0a2b58;
    --banner-light: #0a58ab;
    --banner-dark: #0a3e8b;
    --accent-blue: #0a8fd4;
    --mid-blue: #0b86cf;
    --pale-blue: #d3e8f6;
    --rule-grey: #d9dde2;
    --white: #ffffff;
    --label: #eef4fb;
  }
  * { box-sizing: border-box; margin: 0; padding: 0; }
  html, body { width: 1200px; height: 1200px; overflow: hidden; }
  body {
    position: relative;
    background: radial-gradient(ellipse 75% 55% at 38% 0%, var(--page-glow) 0%, #0a4690 45%, var(--page-deep) 100%);
    font-family: "Hind", Arial, sans-serif;
  }
  .set-label {
    position: absolute;
    left: 91px;
    font-family: "Poppins", Arial, sans-serif;
    font-weight: 300;
    font-size: 25px;
    line-height: 1;
    color: var(--label);
    letter-spacing: -0.2px;
  }
  .banner {
    position: absolute;
    left: 88px;
    width: 1005px;
    height: 143px;
    background: linear-gradient(180deg, var(--banner-light) 0%, var(--banner-dark) 100%);
    box-shadow: 0 8px 14px rgba(0, 15, 40, 0.35);
    overflow: hidden;
  }
  .banner::before {
    content: "";
    position: absolute;
    left: 0; top: 0; bottom: 0;
    width: 11px;
    background: var(--accent-blue);
  }
  .banner-art {
    position: absolute;
    inset: 0;
    width: 100%;
    height: 100%;
  }
  .banner-copy {
    position: absolute;
    left: 27px;
    top: 28px;
    color: var(--white);
    z-index: 2;
  }
  .banner-title {
    font-weight: 700;
    font-size: 47px;
    line-height: 1;
    letter-spacing: -0.6px;
    white-space: nowrap;
  }
  .banner-tagline {
    margin-top: 2px;
    font-weight: 500;
    font-size: 23px;
    line-height: 1.1;
    letter-spacing: -0.3px;
    white-space: nowrap;
  }
</style>
</head>
<body>

  <p class="set-label" style="top:70px">Email signature&nbsp; - 01</p>
  <section class="banner" style="top:129px">
    <svg class="banner-art" viewBox="0 0 1618 230" preserveAspectRatio="none">
      <defs>
        <linearGradient id="weld" x1="0" y1="0" x2="1" y2="1">
          <stop offset="0" stop-color="#5a3a24"/>
          <stop offset="0.45" stop-color="#c86a2c"/>
          <stop offset="0.7" stop-color="#8a4b26"/>
          <stop offset="1" stop-color="#4a3a33"/>
        </linearGradient>
      </defs>
      <polygon points="1033,0 1103,0 1048,70 1060,88 960,88 1000,70" fill="var(--mid-blue)"/>
      <polygon points="1126,0 1236,0 1138,125 1053,125" fill="var(--pale-blue)"/>
      <polygon points="1236,0 1306,0 1226,95 1244,102 1143,230 1073,230 1150,125" fill="var(--mid-blue)"/>
      <polygon points="1043,154 1113,154 1048,230 991,230" fill="var(--pale-blue)"/>
      <polygon points="930,150 1010,150 955,230 873,230" fill="var(--mid-blue)"/>
      <polygon points="1306,0 1343,0 1168,230 1153,230" fill="var(--rule-grey)"/>
      <polygon points="1343,0 1618,0 1618,230 1168,230" fill="url(#weld)" role="img" aria-label="Close-up photo of a copper-coloured weld bead on a steel pipe"/>
      <polygon points="1558,230 1618,230 1618,152" fill="var(--pale-blue)"/>
    </svg>
    <div class="banner-copy">
      <h2 class="banner-title">Piping Spools Fabrication</h2>
      <p class="banner-tagline">Precision Welding for Complex Systems</p>
    </div>
  </section>

  <p class="set-label" style="top:347px">Email signature&nbsp; - 02</p>
  <section class="banner" style="top:394px">
    <svg class="banner-art" viewBox="0 0 1618 230" preserveAspectRatio="none">
      <defs>
        <linearGradient id="frames" x1="0" y1="0" x2="1" y2="1">
          <stop offset="0" stop-color="#2b3f5c"/>
          <stop offset="0.5" stop-color="#7d8ea3"/>
          <stop offset="1" stop-color="#34465e"/>
        </linearGradient>
      </defs>
      <polygon points="1033,0 1103,0 1048,70 1060,88 960,88 1000,70" fill="var(--mid-blue)"/>
      <polygon points="1126,0 1236,0 1138,125 1053,125" fill="var(--pale-blue)"/>
      <polygon points="1236,0 1306,0 1226,95 1244,102 1143,230 1073,230 1150,125" fill="var(--mid-blue)"/>
      <polygon points="1043,154 1113,154 1048,230 991,230" fill="var(--pale-blue)"/>
      <polygon points="930,150 1010,150 955,230 873,230" fill="var(--mid-blue)"/>
      <polygon points="1306,0 1343,0 1168,230 1153,230" fill="var(--rule-grey)"/>
      <polygon points="1343,0 1618,0 1618,230 1168,230" fill="url(#frames)" role="img" aria-label="Photo of welded steel skid frames in a workshop"/>
      <polygon points="1558,230 1618,230 1618,152" fill="var(--pale-blue)"/>
    </svg>
    <div class="banner-copy">
      <h2 class="banner-title">Skid &amp; Frames Fabrication</h2>
      <p class="banner-tagline">Built Strong. Designed Smart.</p>
    </div>
  </section>

  <p class="set-label" style="top:619px">Email signature&nbsp; - 03</p>
  <section class="banner" style="top:666px">
    <svg class="banner-art" viewBox="0 0 1618 230" preserveAspectRatio="none">
      <defs>
        <linearGradient id="tank" x1="0" y1="0" x2="0" y2="1">
          <stop offset="0" stop-color="#3b4e66"/>
          <stop offset="0.4" stop-color="#b9c6d4"/>
          <stop offset="0.75" stop-color="#6f8196"/>
          <stop offset="1" stop-color="#2c3a4e"/>
        </linearGradient>
      </defs>
      <polygon points="1033,0 1103,0 1048,70 1060,88 960,88 1000,70" fill="var(--mid-blue)"/>
      <polygon points="1126,0 1236,0 1138,125 1053,125" fill="var(--pale-blue)"/>
      <polygon points="1236,0 1306,0 1226,95 1244,102 1143,230 1073,230 1150,125" fill="var(--mid-blue)"/>
      <polygon points="1043,154 1113,154 1048,230 991,230" fill="var(--pale-blue)"/>
      <polygon points="930,150 1010,150 955,230 873,230" fill="var(--mid-blue)"/>
      <polygon points="1306,0 1343,0 1168,230 1153,230" fill="var(--rule-grey)"/>
      <polygon points="1343,0 1618,0 1618,230 1168,230" fill="url(#tank)" role="img" aria-label="Photo of a small polished stainless steel tank in a workshop"/>
      <polygon points="1558,230 1618,230 1618,152" fill="var(--pale-blue)"/>
    </svg>
    <div class="banner-copy">
      <h2 class="banner-title">Small Steel Tanks Fabrication</h2>
      <p class="banner-tagline">Compact Strength. Proven Durability.</p>
    </div>
  </section>

  <p class="set-label" style="top:884px">Email signature&nbsp; - 04</p>
  <section class="banner" style="top:932px">
    <svg class="banner-art" viewBox="0 0 1618 230" preserveAspectRatio="none">
      <defs>
        <linearGradient id="workshop" x1="0" y1="0" x2="1" y2="1">
          <stop offset="0" stop-color="#1f2e44"/>
          <stop offset="0.45" stop-color="#5f7ea4"/>
          <stop offset="0.7" stop-color="#2d4564"/>
          <stop offset="1" stop-color="#1a2536"/>
        </linearGradient>
      </defs>
      <polygon points="1033,0 1103,0 1048,70 1060,88 960,88 1000,70" fill="var(--mid-blue)"/>
      <polygon points="1126,0 1236,0 1138,125 1053,125" fill="var(--pale-blue)"/>
      <polygon points="1236,0 1306,0 1226,95 1244,102 1143,230 1073,230 1150,125" fill="var(--mid-blue)"/>
      <polygon points="1043,154 1113,154 1048,230 991,230" fill="var(--pale-blue)"/>
      <polygon points="930,150 1010,150 955,230 873,230" fill="var(--mid-blue)"/>
      <polygon points="1306,0 1343,0 1168,230 1153,230" fill="var(--rule-grey)"/>
      <polygon points="1343,0 1618,0 1618,230 1168,230" fill="url(#workshop)" role="img" aria-label="Photo of a welder at work in a steel fabrication workshop"/>
      <polygon points="1558,230 1618,230 1618,152" fill="var(--pale-blue)"/>
    </svg>
    <div class="banner-copy">
      <h2 class="banner-title">General Fabrication Solutions</h2>
      <p class="banner-tagline">Your Partner in Precision Fabrication</p>
    </div>
  </section>

</body>
</html>
```